Business Card Design Project

I am a Chiropractor that is looking for a new business card.  Our logo was slightly changed lately, therefore need a new, more professional look.
We are a modern, non-stuffy chiropractic office.  Want a contemporary look that will let people know this is not your typical doctors office.  Our logo is red, and contains the name of our business: realign.  The u in the logo is green, stressing the most important part of our business: "u"

Target Market(s)
moderate to upper income bracket, family friendly
www.realignspine-example.com
Gordon Pell
Family Chiropractor
314 Hollis Rd
Bastrop, TX 78999
512.555.0147 phone
512.555.0148 fax
Industry/Entity Type
Business
Requirements
Must have
- www.realignspine-example.com
Gordon Pell
Family Chiropractor
314 Hollis Rd
Bastrop, TX 78999
512.555.0147 phone
512.555.0148 fax

```html
<!DOCTYPE html>
<html lang="en">
<head>
<meta charset="utf-8">
<title>realign — Business Card</title>
<link rel="stylesheet" href="https://fonts.googleapis.com/css2?family=Questrial&display=swap">
<style>
  :root {
    --backdrop: #4b4b4b;
    --card-stock: #e4e4e4;
    --brand-red: #d9262b;
    --brand-green: #5aa63c;
  }
  * { margin: 0; padding: 0; box-sizing: border-box; }
  html, body {
    width: 1200px;
    height: 900px;
    overflow: hidden;
    background: var(--backdrop);
    font-family: "Questrial", "Century Gothic", sans-serif;
  }
  .canvas {
    position: relative;
    width: 1200px;
    height: 900px;
  }
  .card {
    position: absolute;
    top: 300px;
    width: 524px;
    height: 300px;
    border-radius: 18px;
    background: var(--card-stock);
  }
  .card--front { left: 58px; }
  .card--back { left: 617px; }

  .brand-name {
    position: absolute;
    left: 0;
    right: 0;
    top: 118px;
    text-align: center;
    font-size: 52px;
    line-height: 1;
    letter-spacing: 1px;
    color: var(--brand-red);
  }

  .contact-name {
    position: absolute;
    left: 57px;
    top: 180px;
    font-size: 20px;
    font-weight: 700;
    color: var(--brand-green);
    letter-spacing: 0.3px;
  }
  .contact-title {
    position: absolute;
    left: 57px;
    top: 205px;
    font-size: 12.5px;
    color: var(--brand-red);
  }
  .contact-block {
    position: absolute;
    top: 242px;
    font-size: 12.5px;
    line-height: 17px;
    color: var(--brand-red);
    white-space: nowrap;
  }
  .contact-block--address { left: 57px; }
  .contact-block--phones { left: 172px; }
  .contact-label { color: var(--brand-green); }
  .contact-web {
    position: absolute;
    right: 25px;
    top: 256px;
    font-size: 14px;
    font-weight: 700;
    letter-spacing: 0;
    white-space: nowrap;
    color: var(--brand-red);
  }
</style>
</head>
<body>
  <main class="canvas">
    <section class="card card--front" aria-label="Card front">
      <p class="brand-name">realign</p>
    </section>

    <section class="card card--back" aria-label="Card back">
      <p class="contact-name">Gordon Pell</p>
      <p class="contact-title">Family Chiropractor</p>
      <p class="contact-block contact-block--address">314 Hollis Rd<br>Bastrop, TX 78999</p>
      <p class="contact-block contact-block--phones">
        <span class="contact-label">p:</span> 512.555.0147<br>
        <span class="contact-label">f:</span> 512.555.0148
      </p>
      <p class="contact-web">www.realignspine-example.com</p>
    </section>
  </main>
</body>
</html>
```